Snapnook needs You

Help us create an inviting, amazing, sleek, simple, clear landing page for a picture-memory-social connection site!

Business Name: SnapNook
Industry: Social Networking and Creativity through Pictures
A web platform for and about a community that is driven by a passion for sharing, caring, bonding, collaborating, creating and earning with pictures, through pictures and other related creative activities. This is going to be a great site for all creative artists-photographers, artists, graphic artists to express their work and their creativity.

The main focus of the site is - CONNECTIONS.
This will be uncoded.

Desired Website Screen Size
1024x768... Widescreen/Landscape orientation, is what we mean... So it fits on a CPU screen.

Desired look and feel and message
Look: Visitor should feel immersed in the page, in the world the page creates, simple, elegant, sophisticated, contemporary. We really like a clean uncluttered look.

Special mention: By the way we love the marketing genius who thought up this branding for velu yogurt where they used the two dots above the o to create a branding effect that made this brand instantly identifiable. http://www.velu-dairy.ca/en/

The two dots by themselves without having even the name present brings up the whole brand now. The dots are used above all the ingredients of the yogurt creating friendly figures, and above people in commercials-bringing the people onto the side of "team" velu. Snapnook may have a character created or something distinctive in the letters in the name created to brand the site as well.

Feel: Engaging; Magical without being corny, here is a link to give an example look and feel but please do not be hindered in your creativity by this suggestion. We love all creative angles.
http://artscrapheap.com/graphic/5820317-camera-film-roll-blue-background

Message: Life and memories and connections through pictures.

Target audience:
The site is focused on pictures but not confined to photography enthusiasts (although they are an integral part of the site). Customers/Visitors will include families, corporates and the younger generation - all age groups, all class, everyone with pictures to express, memories to share.

Website design we like:
http://morvantstudio.com/work/northern-ballet-guild/
http://morvantstudio.com/work/pixelhop/

What colors do we want to see on our landing page?
We would like the background to be grey or blue since it is grey is picture neutral colour and blue highlights pictures well and we also like blue and silver, which can be integrated into the theme. Also like green. But please do not let these instructions limit your creativity. We are open to new ideas and colours.

Predetermined Concepts if any:
We have a concept in mind and we think it would be cool to have an interface for the user through the back of a camera on the landing page -This could be used to create a scene or world the visitor feels a part of or is immersed into. The back screen of the camera may act as a screen for the slideshow of featured pictures on the site.

Content on the Page:
Photo Gallery with full screen, thumbnail view, zoom option etc.
Prominent but short introductory message
Sign in / Login Options
Links: Home Page; About; Info/Help; Contact Us; Privacy Policy; Terms of Use
At the bottom of the page: Follow Me/Like/Workfolio...social buttons.

Please feel free to add any other element to the landing page that you think might add to the effect of simple yet amazing look -clean, simple, uncluttered, sophisticated, stylish, inviting and engaging.
The concept is a guideline, but we would like you to be as creative as you can, even if it meant stepping out of these guidelines - rethink design, style, content if you like. We believe in bringing a solution in an innovative yet simple and elegant style. Something a visitor would be intrigued enough to explore and the guest would feel comfortable enough taking that step forward to have fun on the site. If you believe in the same, and you have the skill then you will have what we need. Good luck, go for it and we are excited to see what the amazing designers on this amazing site have to offer.
If you have any questions please free to ask.
Updates

HI wanted to send an update that this project design has been guaranteed.

Our site will be one to celebrate and showcase imagination as well as connection.  We would love to see what you create. Keep in mind our site will showcase all creativity, photographs, artists, graphic artists so this would be a benefit you may want to take advantage of in the future, a place where, if you so choose, you could gain exposure for your work. Therefore, even if you do not win the design project there is possible future benefit.

Imagination is everything.
Imagination encircles the world.-Harwood

Reason: We are giving the designers who accepted invites but have not yet submitted a chance to finish their submissions and the ones who are working on revisions a chance to finish those:)

Hello everyone,

Due to time constraints we must come to a decision sooner than the deadline of 28th. 

So, please try to submit any new designs or modifications to the old ones before the 26th. We are very thankful to all of you who have participated - for your designs, enthusiasm and kind words. 

Good luck! :)

• Thank you for the interest shown and your submissions! Designers who have submitted up until now have shown great potential. We are VERY excited with the quality of work and designs.

We want to add that Snapnook is not exclusively for the photographers. The site is for every person who may have a picture to store, organise, use or share - whether publicly or with only a few friends and family.

Snapnook is about allowing people to take control of their creativity. It is about providing tools to our users so that they can build their own connections and social network... of friends, family, fans, clients, ideas, thoughts, emotions etc. through pictures without worrying about their privacy or control over their creations.

With this update we want to encourage others to go beyond the camera theme. Do not let us restrict your creativity. Let YOUR OWN ideas take over if that’s what you think will best convey the message and will appeal to the users.

```html
<!DOCTYPE html>
<html lang="en">
<head>
<meta charset="utf-8">
<title>SnapNook – Landing Page</title>
<link rel="stylesheet" href="https://fonts.googleapis.com/css2?family=Signika:wght@300;400&family=Lato:ital,wght@0,400;1,400&display=swap">
<style>
  :root {
    --page-bg: #2a2a2a;
    --accent-blue: #1fb8ef;
    --accent-blue-dark: #0f8fcd;
    --body-top: #34363a;
    --body-mid: #232427;
    --body-low: #18191b;
    --bezel: #0b0b0c;
    --screen-frame: #e9e4e4;
    --screen-white: #ffffff;
    --ink-dark: #3a3d42;
    --ink-body: #4a4a4a;
    --ink-light: #ffffff;
    --nav-rule: #3e4044;
    --arrow-ink: #b8b8b8;
    --footer-ink: #8a8a8a;
    --footer-rule: #3a3a3a;
  }
  * { box-sizing: border-box; margin: 0; padding: 0; }
  html, body { width: 1200px; height: 950px; overflow: hidden; }
  body {
    position: relative;
    background: var(--page-bg);
    font-family: "Lato", Arial, sans-serif;
  }
  .top-band { position: absolute; left: 0; top: 0; width: 1200px; height: 13px; background: var(--accent-blue); }

  .camera-body {
    position: absolute; left: 90px; top: 64px; width: 1010px; height: 769px;
    border-radius: 60px;
    background: linear-gradient(180deg, var(--body-top), var(--body-mid) 50%, var(--body-low));
  }

  .play-button { position: absolute; left: 975px; top: 208px; }

  .screen-bezel {
    position: absolute; left: 155px; top: 198px; width: 624px; height: 590px;
    background: var(--bezel); border-radius: 10px;
  }
  .screen {
    position: absolute; left: 163px; top: 206px; width: 603px; height: 577px;
    background: var(--screen-frame); border-radius: 8px; padding: 7px;
  }
  .screen-inner {
    position: relative; width: 100%; height: 100%;
    background: var(--screen-white); border-radius: 6px;
  }
  .intro-quote {
    position: absolute; left: 21px; top: 16px;
    font-family: "Signika", Arial, sans-serif; font-weight: 400;
    font-size: 24.5px; line-height: 30px; color: var(--ink-dark);
  }
  .intro-text {
    position: absolute; left: 23px; top: 80px; width: 545px;
    font-size: 13.2px; line-height: 22px; color: var(--ink-body);
  }
  .section-title {
    position: absolute; left: 25px;
    font-family: "Signika", Arial, sans-serif; font-weight: 400;
    font-size: 18.5px; color: var(--ink-dark);
  }
  .title-viewed { top: 138px; }
  .title-photographers { top: 367px; }

  .thumb-grid {
    position: absolute; left: 25px; top: 171px;
    display: grid; grid-template-columns: repeat(6, 83px); grid-auto-rows: 83px; gap: 3px;
  }
  .thumb { display: block; }
  .t-red { background: linear-gradient(135deg, #d9332e, #4f8a2c); }
  .t-warm { background: linear-gradient(160deg, #c98a4a, #8f5125); }
  .t-night { background: linear-gradient(180deg, #151515, #3a2f1a 80%, #151515); }
  .t-night2 { background: linear-gradient(180deg, #0d0d10, #2a2420 70%, #0d0d10); }
  .t-cafe { background: linear-gradient(160deg, #7fa7c4, #3b6d94); }
  .t-shallow { background: linear-gradient(160deg, #a9b9ae, #6e8d86); }
  .t-deck { background: linear-gradient(160deg, #cfd6dc, #3d4f66); }
  .t-wave { background: linear-gradient(180deg, #8fbfe0, #cfe3ec); }
  .t-wave2 { background: linear-gradient(180deg, #cfe3ec, #6fa8c8); }
  .t-shore { background: linear-gradient(180deg, #5aa6c9, #bfc9c2); }
  .t-bay { background: linear-gradient(180deg, #9fb7c8, #5a8a3a 45%, #3f93c0); }
  .t-deep { background: linear-gradient(160deg, #1f5fb3, #2f86c8 70%, #3d6a2e); }

  .scroll-arrows { position: absolute; }
  .arrows-viewed { left: 547px; top: 317px; }
  .arrows-photographers { left: 543px; top: 472px; }

  .photographer-row { position: absolute; left: 24px; top: 403px; display: flex; gap: 8.5px; }
  .photographer { width: 96px; }
  .portrait { display: block; width: 96px; height: 92px; }
  .p1 { background: linear-gradient(160deg, #3d6f9c, #d9a77a); }
  .p2 { background: linear-gradient(160deg, #7a5a3a, #2a2a2a); }
  .p3 { background: linear-gradient(160deg, #c9d8e6, #8a2f2f); }
  .p4 { background: linear-gradient(160deg, #f0f0f0, #2a2a2a); }
  .p5 { background: linear-gradient(160deg, #e6d45a, #3a3a3a); }
  .user-name { display: block; margin-top: 6px; font-size: 12px; color: var(--ink-body); }

  .brand {
    position: absolute; left: 815px; top: 298px;
    display: flex; align-items: center; gap: 10px;
    font-family: "Signika", Arial, sans-serif; font-weight: 400;
    font-size: 50px; line-height: 1; color: var(--ink-light);
  }
  .brand-dot { width: 12px; height: 12px; border-radius: 50%; background: var(--accent-blue); }

  .main-nav { position: absolute; left: 816px; top: 370px; width: 174px; list-style: none; }
  .main-nav li {
    height: 35.2px; display: flex; align-items: center; gap: 17px;
    border-bottom: 1px solid var(--nav-rule);
    font-family: "Signika", Arial, sans-serif; font-weight: 300;
    font-size: 17px; color: var(--ink-light);
  }
  .main-nav li:last-child { border-bottom: none; }
  .main-nav li.is-current { color: var(--accent-blue); }

  .upload-label {
    position: absolute; left: 817px; top: 609px;
    font-family: "Signika", Arial, sans-serif; font-weight: 300;
    font-size: 15px; color: var(--ink-light);
  }
  .upload-field {
    position: absolute; left: 814px; top: 636px; width: 247px; height: 29px;
    background: var(--screen-white); border-radius: 3px;
    display: flex; align-items: center; justify-content: space-between; padding: 0 12px 0 14px;
    font-style: italic; font-size: 12px; color: #8a8a8a;
  }
  .panel-rule { position: absolute; left: 869px; top: 691px; width: 165px; height: 1px; background: var(--nav-rule); }
  .sign-in {
    position: absolute; left: 826px; top: 707px; width: 83px; height: 34px;
    border-radius: 3px; background: linear-gradient(180deg, var(--accent-blue), var(--accent-blue-dark));
    display: flex; align-items: center; justify-content: center;
    font-family: "Signika", Arial, sans-serif; font-weight: 400;
    font-size: 16px; color: var(--ink-light);
  }
  .social-links { position: absolute; left: 922px; top: 712px; display: flex; gap: 5px; }
  .social-button { width: 24px; height: 24px; border-radius: 50%; background: var(--ink-light); }

  .footer-rule { position: absolute; left: 0; top: 889px; width: 1200px; height: 1px; background: var(--footer-rule); }
  .footer-note {
    position: absolute; left: 0; top: 910px; width: 1208px; text-align: center;
    font-size: 11.5px; color: var(--footer-ink);
  }
</style>
</head>
<body>
  <div class="top-band"></div>

  <div class="camera-body" role="img" aria-label="Photo of the back of a dark digital camera body framing the page"></div>

  <svg class="play-button" width="60" height="60" viewBox="0 0 60 60" aria-hidden="true">
    <circle cx="30" cy="30" r="29" fill="#0c0c0d" stroke="#3a3c40" stroke-width="2"/>
    <rect x="17" y="20" width="26" height="20" fill="none" stroke="#6f9fd6" stroke-width="2"/>
    <path d="M25 24 L36 30 L25 36 Z" fill="#6f9fd6"/>
  </svg>

  <div class="screen-bezel"></div>
  <main class="screen">
    <div class="screen-inner">
      <h1 class="intro-quote">Imagination is everything.<br>Imagination encircles the world.- Albert Harwood</h1>
      <p class="intro-text">Lorem ipsum dolor sit amet, consectetuer adipiscing elit. Nam cursus. Morbi ut mi. Nullam enim leo, egestas id, condimentum at, laoreet mattis, massa. Sed eleifend</p>

      <h2 class="section-title title-viewed">Most Viewed</h2>
      <div class="thumb-grid">
        <span class="thumb t-red" role="img" aria-label="Red hibiscus flower"></span>
        <span class="thumb t-warm" role="img" aria-label="Warm orange textured surface"></span>
        <span class="thumb t-night" role="img" aria-label="Harbour lights at night"></span>
        <span class="thumb t-night2" role="img" aria-label="Waterfront at night"></span>
        <span class="thumb t-cafe" role="img" aria-label="Seaside café tables"></span>
        <span class="thumb t-shallow" role="img" aria-label="Clear shallow water"></span>
        <span class="thumb t-deck" role="img" aria-label="Relaxing on a deck chair"></span>
        <span class="thumb t-wave" role="img" aria-label="Breaking wave"></span>
        <span class="thumb t-wave2" role="img" aria-label="Sea foam"></span>
        <span class="thumb t-shore" role="img" aria-label="Turquoise shoreline"></span>
        <span class="thumb t-bay" role="img" aria-label="Bay with hills and a boat"></span>
        <span class="thumb t-deep" role="img" aria-label="Deep blue sea by the coast"></span>
      </div>
      <svg class="scroll-arrows arrows-viewed" width="16" height="20" viewBox="0 0 16 20" aria-hidden="true">
        <path d="M1 7 L8 1 L15 7 M1 13 L8 19 L15 13" fill="none" stroke="#b8b8b8" stroke-width="1.2"/>
      </svg>

      <h2 class="section-title title-photographers">Best Photographers</h2>
      <div class="photographer-row">
        <div class="photographer"><span class="portrait p1" role="img" aria-label="Photographer portrait"></span><span class="user-name">User Name</span></div>
        <div class="photographer"><span class="portrait p2" role="img" aria-label="Photographer portrait"></span><span class="user-name">User Name</span></div>
        <div class="photographer"><span class="portrait p3" role="img" aria-label="Photographer portrait"></span><span class="user-name">User Name</span></div>
        <div class="photographer"><span class="portrait p4" role="img" aria-label="Photographer portrait"></span><span class="user-name">User Name</span></div>
        <div class="photographer"><span class="portrait p5" role="img" aria-label="Photographer portrait"></span><span class="user-name">User Name</span></div>
      </div>
      <svg class="scroll-arrows arrows-photographers" width="16" height="20" viewBox="0 0 16 20" aria-hidden="true">
        <path d="M1 7 L8 1 L15 7 M1 13 L8 19 L15 13" fill="none" stroke="#b8b8b8" stroke-width="1.2"/>
      </svg>
    </div>
  </main>

  <div class="brand"><span class="brand-dot"></span>SnapNook</div>

  <ul class="main-nav">
    <li class="is-current"><svg width="16" height="13" viewBox="0 0 16 13" aria-hidden="true"><rect x="0.5" y="0.5" width="15" height="12" fill="none" stroke="#8a8c90"/><path d="M5 3 L11 6.5 L5 10 Z" fill="#8a8c90"/></svg>Home</li>
    <li><svg width="16" height="13" viewBox="0 0 16 13" aria-hidden="true"><rect x="0.5" y="0.5" width="15" height="12" fill="none" stroke="#6a6c70"/><path d="M5 3 L11 6.5 L5 10 Z" fill="#6a6c70"/></svg>About</li>
    <li><svg width="16" height="13" viewBox="0 0 16 13" aria-hidden="true"><rect x="0.5" y="0.5" width="15" height="12" fill="none" stroke="#6a6c70"/><path d="M5 3 L11 6.5 L5 10 Z" fill="#6a6c70"/></svg>Help</li>
    <li><svg width="16" height="13" viewBox="0 0 16 13" aria-hidden="true"><rect x="0.5" y="0.5" width="15" height="12" fill="none" stroke="#6a6c70"/><path d="M5 3 L11 6.5 L5 10 Z" fill="#6a6c70"/></svg>Contact Us</li>
    <li><svg width="16" height="13" viewBox="0 0 16 13" aria-hidden="true"><rect x="0.5" y="0.5" width="15" height="12" fill="none" stroke="#6a6c70"/><path d="M5 3 L11 6.5 L5 10 Z" fill="#6a6c70"/></svg>Privacy Policy</li>
    <li><svg width="16" height="13" viewBox="0 0 16 13" aria-hidden="true"><rect x="0.5" y="0.5" width="15" height="12" fill="none" stroke="#6a6c70"/><path d="M5 3 L11 6.5 L5 10 Z" fill="#6a6c70"/></svg>Terms of Use</li>
  </ul>

  <p class="upload-label">Upload your photo</p>
  <div class="upload-field">photo upload now
    <svg width="7" height="12" viewBox="0 0 7 12" aria-hidden="true"><path d="M0 0 L7 6 L0 12 Z" fill="#9a9a9a"/></svg>
  </div>
  <div class="panel-rule"></div>
  <div class="sign-in">Sign in</div>
  <div class="social-links">
    <span class="social-button"></span>
    <span class="social-button"></span>
    <span class="social-button"></span>
    <span class="social-button"></span>
  </div>

  <div class="footer-rule"></div>
  <footer class="footer-note">© 2012 Company Name.&nbsp; All right reserved.&nbsp; Term of Use</footer>
</body>
</html>
```